" Empresa focada em seguros pessoais, tais como seguro saúde, vida, previdência e odontológico, oferecendo segurança e agilidade na contrataçao e manutençao e também qualidade de vida. "

```html
<!DOCTYPE html>
<html lang="pt-BR">
<head>
<meta charset="utf-8">
<title>CelesteVida – Pasta com Bolsa</title>
<link rel="stylesheet" href="https://fonts.googleapis.com/css2?family=Titillium+Web:wght@400;600&display=swap">
<style>
  :root {
    --bg: #e6e7e9;
    --cyan: #21b5cc;
    --navy: #0d3277;
    --navy-soft: #1a4a92;
    --white: #ffffff;
    --font: "Titillium Web", Arial, sans-serif;
  }
  html, body {
    margin: 0;
    width: 1200px;
    height: 1200px;
    overflow: hidden;
    background: var(--bg);
    font-family: var(--font);
  }
  .folder {
    position: relative;
    width: 1200px;
    height: 1200px;
  }
  .folder-shapes {
    position: absolute;
    inset: 0;
  }
  .brand {
    position: absolute;
    display: flex;
    align-items: center;
    gap: 10px;
  }
  .brand-mark {
    border-radius: 50%;
    flex: none;
  }
  .brand-name {
    font-weight: 600;
    line-height: 1;
  }
  .brand-tagline {
    font-weight: 400;
    line-height: 1.1;
  }
  .brand--cover {
    left: 744px;
    top: 300px;
    color: var(--cyan);
  }
  .brand--cover .brand-mark {
    width: 46px;
    height: 46px;
    background: var(--cyan);
  }
  .brand--cover .brand-name { font-size: 44px; }
  .brand--cover .brand-tagline { font-size: 15px; letter-spacing: 0.5px; }
  .brand--back {
    left: 176px;
    top: 822px;
    color: var(--white);
  }
  .brand--back .brand-mark {
    width: 28px;
    height: 28px;
    background: var(--white);
  }
  .brand--back .brand-name { font-size: 30px; }
  .brand--back .brand-tagline { font-size: 9px; }
  .contact {
    position: absolute;
    left: 420px;
    top: 808px;
    margin: 0;
    color: var(--white);
    font-size: 9.5px;
    line-height: 1.45;
    font-style: normal;
  }
</style>
</head>
<body>
<main class="folder">
  <svg class="folder-shapes" width="1200" height="1200" viewBox="0 0 1200 1200">
    <defs>
      <linearGradient id="illustration-fill" x1="0" y1="0" x2="1" y2="1">
        <stop offset="0" stop-color="#0d3277"/>
        <stop offset="0.6" stop-color="#1a4a92"/>
        <stop offset="1" stop-color="#21b5cc"/>
      </linearGradient>
    </defs>
    <rect class="panel-back" x="96" y="108" width="523" height="775" fill="var(--cyan)"/>
    <rect class="panel-cover" x="619" y="108" width="509" height="775" fill="var(--white)"/>
    <rect class="illustration" role="img" aria-label="Ilustração de uma árvore estilizada com copas em azul-marinho e azul-claro atravessando as duas faces da pasta"
          x="350" y="410" width="500" height="375" rx="170" fill="url(#illustration-fill)" opacity="0.9"/>
    <path class="pocket-band" d="M619,836 L1064,836 Q1114,836 1128,883 L619,883 Z" fill="var(--navy)"/>
    <path class="pocket-flap" d="M72,905 L96,883 L619,883 L619,905 Q626,1000 590,1070 Q560,1122 500,1128 L72,1128 Z" fill="var(--navy)"/>
    <path class="pocket-flap-edge" d="M72,905 L96,883 L619,883 L619,905 Z" fill="var(--navy-soft)"/>
  </svg>

  <div class="brand brand--cover">
    <span class="brand-mark"></span>
    <div>
      <div class="brand-name">CelesteVida</div>
      <div class="brand-tagline">Consultoria de Benefícios</div>
    </div>
  </div>

  <div class="brand brand--back">
    <span class="brand-mark"></span>
    <div>
      <div class="brand-name">CelesteVida</div>
      <div class="brand-tagline">Consultoria de Benefícios</div>
    </div>
  </div>

  <address class="contact">
    Av. Horizonte, 120<br>
    (11) 4000-1000<br>
    (11) 4000-2000<br>
    contato@celestevida.com.br<br>
    <strong>www.celestevida.com.br</strong>
  </address>
</main>
</body>
</html>
```